One of Australia's fastest growing Financial Company looking for an updated business card design!

Meridale Holdings Australia is looking for an updated design for our business cards. We would like to keep up our professional appearances and have get new exciting design that fits our company.

The Meridale aim is to facilitate and assist clients in every financial requirement that may arise in financial areas.

We would to see the design to use colour blue and we like the clouds in the background. We have attached two designs we have use before but we need something with more professional and easy to read design.

We would like the website in the back of the card; the employees name more central and stands out; only a postal address; a list of all our locations along the bottom (Sydney, Melbourne, Brisbane, Singapore)

Looking forward to seeing the designs come in!

Target Market(s)

Other Industry Professionals
Middle Class Families

Industry/Entity Type

Finance

Contact Information for Business Card

Name; Company Role; Office Number; Mobile Number; Email Address; Website; Postal Address; Locations

Font styles to use
Serif
Sans Serif

Colors
0492cd
33a6d7
85cae6
85acd3
3176b5
0455a3
cee9f5
d5e2ee

Requirements
Must have
• Name; Company Role; Office Number; Mobile Number; Email Address; Website; Postal Address; Locations
Nice to have
• The colour blue, clouds on the background

```html
<!DOCTYPE html>
<html lang="en">
<head>
<meta charset="utf-8">
<title>Meridale Holdings Australia – Business Card</title>
<link rel="stylesheet" href="https://fonts.googleapis.com/css2?family=Lato:wght@400;700;900&display=swap">
<style>
  :root {
    --stage: #2b2b2d;
    --band: #2a88c6;
    --rule: #d8393c;
    --white: #ffffff;
    --navy: #0b2f52;
  }
  html, body {
    margin: 0;
    width: 1200px;
    height: 997px;
    overflow: hidden;
    background: var(--stage);
  }
  .stage {
    position: relative;
    width: 1200px;
    height: 997px;
  }
  .card {
    position: absolute;
    width: 560px;
    height: 320px;
    box-shadow: 0 18px 40px rgba(0,0,0,.55);
  }
  .card--front { left: 80px; top: 110px; }
  .card--back  { left: 560px; top: 520px; }
  .card svg { display: block; width: 560px; height: 320px; }
  .brand {
    font-family: "Lato", sans-serif;
    font-weight: 700;
    fill: var(--white);
  }
  .locations {
    font-family: "Lato", sans-serif;
    font-size: 13px;
    letter-spacing: 1.5px;
    fill: var(--white);
  }
  .locations .sep { fill: var(--rule); }
  .contact {
    font-family: "Lato", sans-serif;
    font-size: 12.5px;
    letter-spacing: .5px;
    fill: var(--white);
  }
  .address {
    font-family: "Lato", sans-serif;
    font-size: 12.5px;
    letter-spacing: .5px;
    fill: var(--white);
  }
  .holder-name {
    font-family: "Lato", sans-serif;
    font-weight: 900;
    font-size: 20px;
    fill: var(--white);
  }
  .holder-role {
    font-family: "Lato", sans-serif;
    font-weight: 400;
    font-size: 14px;
    fill: var(--navy);
  }
  .icon { fill: var(--white); }
</style>
</head>
<body>
<main class="stage">

  <section class="card card--front">
    <svg viewBox="0 0 560 320" xmlns="http://www.w3.org/2000/svg">
      <defs>
        <radialGradient id="skyFront" cx="0.3" cy="0.38" r="0.85">
          <stop offset="0" stop-color="#ffffff"/>
          <stop offset="0.18" stop-color="#cee9f5"/>
          <stop offset="0.5" stop-color="#85acd3"/>
          <stop offset="1" stop-color="#3176b5"/>
        </radialGradient>
        <path id="frontCityPath" d="M 150 318 Q 400 285 560 150"/>
      </defs>
      <rect class="sky" width="560" height="320" fill="url(#skyFront)" role="img" aria-label="Photograph of a bright blue sky with white clouds and sun rays"/>
      <path class="band" d="M 0 300 Q 330 275 560 105 L 560 320 L 0 320 Z" fill="var(--band)"/>
      <path class="band-rule" d="M 0 300 Q 330 275 560 105" fill="none" stroke="var(--rule)" stroke-width="3"/>
      <g class="logo" transform="translate(190 185) rotate(-22)">
        <circle cx="0" cy="-12" r="12" fill="var(--rule)"/>
        <text class="brand" x="22" y="0" font-size="46">Meridale</text>
      </g>
      <text class="locations">
        <textPath href="#frontCityPath" startOffset="8%">Sydney <tspan class="sep">•</tspan> Melbourne <tspan class="sep">•</tspan> Brisbane <tspan class="sep">•</tspan> Singapore</textPath>
      </text>
    </svg>
  </section>

  <section class="card card--back">
    <svg viewBox="0 0 560 320" xmlns="http://www.w3.org/2000/svg">
      <defs>
        <radialGradient id="skyBack" cx="0.3" cy="0.3" r="0.85">
          <stop offset="0" stop-color="#ffffff"/>
          <stop offset="0.18" stop-color="#cee9f5"/>
          <stop offset="0.5" stop-color="#85acd3"/>
          <stop offset="1" stop-color="#3176b5"/>
        </radialGradient>
      </defs>
      <rect class="sky" width="560" height="320" fill="url(#skyBack)" role="img" aria-label="Photograph of a bright blue sky with white clouds and sun rays"/>
      <path class="band" d="M 0 228 Q 300 270 560 60 L 560 320 L 0 320 Z" fill="var(--band)"/>
      <path class="band-rule" d="M 0 228 Q 300 270 560 60" fill="none" stroke="var(--rule)" stroke-width="3"/>

      <g class="logo" transform="translate(150 150) rotate(-14)">
        <circle cx="0" cy="-12" r="12" fill="var(--rule)"/>
        <text class="brand" x="22" y="0" font-size="44">Meridale</text>
      </g>

      <g class="contacts" text-anchor="end">
        <text class="contact" x="520" y="188">+1 (203) 555-0142</text>
        <rect class="icon" x="528" y="179" width="10" height="7" rx="1.5"/>
        <text class="contact" x="520" y="210">+1 (914) 555-0187</text>
        <rect class="icon" x="530" y="200" width="6" height="11" rx="1.2"/>
        <text class="contact" x="520" y="232">care@meridale.com</text>
        <rect class="icon" x="528" y="224" width="10" height="7"/>
        <text class="contact" x="520" y="254">www.meridale.com.au</text>
        <circle class="icon" cx="533" cy="250" r="4.5"/>
      </g>

      <text class="address" x="538" y="296" text-anchor="end">42 Alder Creek Road, 2nd Floor, Easton, CT 06612</text>

      <g class="holder">
        <text class="holder-name" x="28" y="282">Lena Marlowe</text>
        <text class="holder-role" x="28" y="302">Managing Partner</text>
      </g>
    </svg>
  </section>

</main>
</body>
</html>
```